Property Management business needs Business cards designed

We provide a premium property management service based in Sydney's Norther Beaches. We want people to feel confident in choosing us to manage their investment properties. We offer a much more personalized service than other estate agents.
We want a modern clean design. Something that shows confidence without being complicated.
Logo attached.

Target Market(s)

35-70yo Male and Female with strong property portfolios within Sydney's Norther Beaches

Industry/Entity Type

Property Management

Contact Information for Business Card

Address: Suite 7, 12-14 Kelvin Parade, Harlow NSW 2188
Two separate named cards.
Tom Ardley - 0491 570 118 tom@harbourvaleestates.com.au
Clara Dunmore - 0491 570 263 clara@harbourvaleestates.com.au

Requirements
Must have
• Business logo, name, number, address, email.

```html
<!DOCTYPE html>
<html lang="en">
<head>
<meta charset="utf-8">
<title>Harbourvale Estates – Business Cards</title>
<link href="https://fonts.googleapis.com/css2?family=Arimo:wght@400;700&display=swap" rel="stylesheet">
<style>
  :root {
    --backdrop: #d9d4cc;
    --card-black: #050505;
    --teal: #2e97a2;
    --cream: #e4e0d4;
    --logo-grey: #dcdad2;
    --text-white: #f2f2f2;
    --divider: #9a9a9a;
  }
  html, body {
    margin: 0;
    width: 1200px;
    height: 902px;
    overflow: hidden;
    background: var(--backdrop);
    font-family: "Arimo", Arial, sans-serif;
  }
  .icon-defs {
    position: absolute;
    width: 0;
    height: 0;
  }
  .card {
    position: absolute;
    left: 270px;
    width: 660px;
    height: 403px;
    background: var(--card-black);
    box-shadow: 0 10px 24px rgba(0,0,0,0.35);
    overflow: hidden;
  }
  .card--clara { top: 33px; }
  .card--tom { top: 466px; }
  .card-waves {
    position: absolute;
    inset: 0;
  }
  .divider {
    position: absolute;
    left: 264px;
    top: 26px;
    width: 1px;
    height: 250px;
    background: var(--divider);
  }
  .brand {
    position: absolute;
    left: 26px;
    top: 148px;
    width: 230px;
    display: flex;
    align-items: center;
    gap: 12px;
  }
  .brand-dot {
    width: 22px;
    height: 22px;
    border-radius: 50%;
    background: var(--teal);
    flex: none;
  }
  .brand-name {
    color: var(--logo-grey);
    font-weight: 700;
    font-size: 23px;
    line-height: 1.08;
    letter-spacing: 1px;
  }
  .contact {
    position: absolute;
    right: 26px;
    top: 26px;
    text-align: right;
  }
  .contact-name {
    color: var(--teal);
    font-size: 28px;
    margin: 0 0 8px;
    font-weight: 400;
  }
  .contact-line {
    color: var(--text-white);
    font-size: 15px;
    margin: 0 0 5px;
    display: flex;
    justify-content: flex-end;
    align-items: center;
    gap: 8px;
  }
  .icon {
    width: 12px;
    height: 12px;
    flex: none;
  }
  .address {
    position: absolute;
    right: 26px;
    bottom: 24px;
    color: var(--text-white);
    font-size: 20px;
    margin: 0;
  }
</style>
</head>
<body>
  <svg class="icon-defs" aria-hidden="true">
    <symbol id="icon-phone" viewBox="0 0 16 16">
      <rect width="16" height="16" rx="2" fill="#e4e0d4"/>
      <path d="M5 3 L7 3 L7.5 6 L6.3 7 C7 8.5 7.8 9.3 9 10 L10 8.7 L13 9.2 L13 11.3 C8 12 4 8 5 3 Z" fill="#050505"/>
    </symbol>
    <symbol id="icon-mail" viewBox="0 0 16 16">
      <rect width="16" height="16" rx="2" fill="#e4e0d4"/>
      <rect x="3" y="5" width="10" height="7" fill="none" stroke="#050505" stroke-width="1.2"/>
      <path d="M3 5 L8 9 L13 5" fill="none" stroke="#050505" stroke-width="1.2"/>
    </symbol>
  </svg>

  <div class="card card--clara">
    <svg class="card-waves" viewBox="0 0 1000 610" width="660" height="403" preserveAspectRatio="none" aria-hidden="true">
      <path d="M0,470 C250,450 620,430 1000,270 L1000,610 L0,610 Z" fill="var(--cream)"/>
      <path d="M0,485 C260,465 640,450 1000,320 L1000,610 L0,610 Z" fill="var(--card-black)"/>
      <path d="M0,500 C280,485 660,470 1000,360 L1000,610 L0,610 Z" fill="var(--teal)"/>
    </svg>
    <div class="divider"></div>
    <div class="brand">
      <span class="brand-dot"></span>
      <span class="brand-name">HARBOURVALE<br>ESTATES</span>
    </div>
    <div class="contact">
      <p class="contact-name">Clara Dunmore</p>
      <p class="contact-line">0491 570 263 <svg class="icon"><use href="#icon-phone"/></svg></p>
      <p class="contact-line">clara@harbourvaleestates.com.au <svg class="icon"><use href="#icon-mail"/></svg></p>
    </div>
    <p class="address">Suite 7, 12-14 Kelvin Parade, Harlow NSW 2188</p>
  </div>

  <div class="card card--tom">
    <svg class="card-waves" viewBox="0 0 1000 610" width="660" height="403" preserveAspectRatio="none" aria-hidden="true">
      <path d="M0,470 C250,450 620,430 1000,270 L1000,610 L0,610 Z" fill="var(--cream)"/>
      <path d="M0,485 C260,465 640,450 1000,320 L1000,610 L0,610 Z" fill="var(--card-black)"/>
      <path d="M0,500 C280,485 660,470 1000,360 L1000,610 L0,610 Z" fill="var(--teal)"/>
    </svg>
    <div class="divider"></div>
    <div class="brand">
      <span class="brand-dot"></span>
      <span class="brand-name">HARBOURVALE<br>ESTATES</span>
    </div>
    <div class="contact">
      <p class="contact-name">Tom Ardley</p>
      <p class="contact-line">0491 570 118 <svg class="icon"><use href="#icon-phone"/></svg></p>
      <p class="contact-line">tom@harbourvaleestates.com.au <svg class="icon"><use href="#icon-mail"/></svg></p>
    </div>
    <p class="address">Suite 7, 12-14 Kelvin Parade, Harlow NSW 2188</p>
  </div>
</body>
</html>
```